Corwyns Best 4 years in a row

I need a billboard that has all the attached logos and says:

Corwyn's Best Realtor 4 Years in a row!

1.75 Listing Fee

Tobias Wrenfield

555-214-7390

and somewhere very small at the bottom:

855-555-0142

2748 W Amberlow Rd, Larkmoor, QX 20957

I put in the last winner just to give an idea of what I'm looking for, although I'd like to switch it up a little bit.

```html
<!DOCTYPE html>
<html lang="en">
<head>
<meta charset="utf-8">
<title>Corwyn's Best Realtor Billboard</title>
<link rel="stylesheet" href="https://fonts.googleapis.com/css2?family=Fraunces:opsz,wght@9..144,400;9..144,500;9..144,700&display=swap">
<style>
  :root {
    --navy: #1d3461;
    --band-grey: #9d9d9d;
    --name-grey: #8c8c8c;
    --white: #ffffff;
    --page: #ececec;
    --badge: #1f1f1f;
  }
  * { margin: 0; padding: 0; box-sizing: border-box; }
  html, body {
    width: 1200px;
    height: 1200px;
    overflow: hidden;
    background: var(--page);
    font-family: "Fraunces", Georgia, serif;
  }
  .billboard {
    position: absolute;
    left: 0;
    top: 421px;
    width: 1200px;
    height: 358px;
    background: var(--white);
    overflow: hidden;
  }
  .billboard-shapes {
    position: absolute;
    inset: 0;
    width: 100%;
    height: 100%;
  }
  .brand {
    position: absolute;
    left: 0;
    top: 52px;
    width: 236px;
    display: flex;
    flex-direction: column;
    align-items: center;
    color: var(--navy);
    font-weight: 500;
    font-size: 17px;
    letter-spacing: 1.5px;
    text-transform: uppercase;
    text-align: center;
    line-height: 1.3;
  }
  .brand-mark {
    width: 46px;
    height: 46px;
    border-radius: 50%;
    background: var(--navy);
    margin-bottom: 12px;
  }
  .headline {
    position: absolute;
    left: 285px;
    top: 30px;
    color: var(--white);
    line-height: 1.12;
  }
  .headline-place,
  .headline-streak {
    font-size: 42px;
    font-weight: 400;
  }
  .headline-title {
    font-size: 46px;
    font-weight: 700;
    letter-spacing: 0.5px;
  }
  .listing-fee {
    position: absolute;
    left: 287px;
    top: 207px;
    color: var(--white);
    font-size: 25px;
    font-weight: 400;
  }
  .footer-contact {
    position: absolute;
    left: 40px;
    top: 308px;
    color: var(--white);
    font-size: 17px;
    font-weight: 400;
  }
  .agent-photo {
    position: absolute;
    left: 688px;
    top: 21px;
    width: 215px;
    height: 337px;
    border-radius: 90px 90px 0 0;
    background: linear-gradient(180deg, #c9a58a 0%, #5a6a85 30%, #2c3a55 100%);
  }
  .agent {
    position: absolute;
    left: 900px;
    top: 34px;
    width: 284px;
    text-align: center;
  }
  .agent-name {
    color: var(--name-grey);
    font-size: 28px;
    font-weight: 400;
  }
  .agent-phone {
    color: var(--navy);
    font-size: 31px;
    font-weight: 700;
    margin-top: 2px;
  }
  .award-badge {
    position: absolute;
    left: 956px;
    top: 139px;
    width: 172px;
    height: 172px;
    border-radius: 50%;
    background: var(--badge);
  }
</style>
</head>
<body>
  <div class="billboard">
    <svg class="billboard-shapes" viewBox="0 0 1200 358" preserveAspectRatio="none" aria-hidden="true">
      <polygon fill="var(--navy)" points="236,0 645,0 972,358 664,358 588,274 236,274"/>
      <polygon fill="var(--band-grey)" points="0,299 580,299 620,340 0,340"/>
    </svg>

    <div class="brand">
      <span class="brand-mark"></span>
      <span class="brand-name">Summit Team</span>
      <span class="brand-name">Keystone Realty</span>
    </div>

    <h1 class="headline">
      <div class="headline-place">Corwyn's</div>
      <div class="headline-title">BEST REALTOR</div>
      <div class="headline-streak">4 Years in a row!</div>
    </h1>

    <p class="listing-fee">1.75 Listing Fee</p>

    <p class="footer-contact">855-555-0142 | 2748 W Amberlow Rd, Larkmoor, QX 20957</p>

    <div class="agent-photo" role="img" aria-label="Portrait photo of the realtor in a navy suit"></div>

    <div class="agent">
      <p class="agent-name">Tobias Wrenfield</p>
      <p class="agent-phone">555-214-7390</p>
    </div>

    <div class="award-badge" role="img" aria-label="Award winner badge"></div>
  </div>
</body>
</html>
```